Laundromat washing machine soap instructions poster

I own a laundromat and need a poster explaining to my customers how to load the soap, bleach and fabric softener into our washing machines. I tried to make a poster on canva but it looks terrible. My Laundromat is called "Tidal Lane" and would like my logo to also be on the poster for branding. I would like the poster to use my blue logo colors to match my brand identity.
Under the photo please include the following text:
" *Please place pods inside the washer"
Thanks

```html
<!DOCTYPE html>
<html lang="en">
<head>
<meta charset="utf-8">
<title>Tidal Lane – Where does the soap go?</title>
<link rel="stylesheet" href="https://fonts.googleapis.com/css2?family=Exo+2:ital,wght@0,600;0,700;0,800;1,800;1,900&display=swap">
<style>
  :root {
    --deep-blue: #12a7dc;
    --mid-blue: #6ecdee;
    --pale-blue: #c8e9f8;
    --mist-blue: #ebf7fc;
    --callout-blue: #18a8dc;
    --brand-blue: #2273b8;
    --ink: #000000;
    --tray-grey: #6b6d70;
    --tray-light: #c9cbcc;
  }
  * { margin: 0; padding: 0; box-sizing: border-box; }
  html, body { width: 800px; height: 1200px; overflow: hidden; }
  body { font-family: "Exo 2", sans-serif; background: var(--mist-blue); }
  .poster { position: relative; width: 800px; height: 1200px; overflow: hidden; }
  .backdrop { position: absolute; inset: 0; }
  .headline {
    position: absolute; left: 40px; top: 20px;
    font-size: 168px; font-weight: 900; font-style: italic;
    letter-spacing: -2px; line-height: 1; color: var(--ink);
  }
  .subhead {
    position: absolute; left: 118px; top: 200px;
    font-size: 56px; font-weight: 800; font-style: italic;
    color: var(--ink); line-height: 1; white-space: nowrap;
  }
  .subhead .emphasis { font-size: 84px; }
  .dispenser-photo {
    position: absolute; left: 24px; top: 390px; width: 388px; height: 496px;
    background: linear-gradient(160deg, var(--tray-grey) 0%, #8a8c8f 45%, var(--tray-light) 70%, var(--tray-grey) 100%);
    border-radius: 10px;
  }
  .callouts { position: absolute; inset: 0; }
  .label {
    position: absolute; left: 488px;
    font-size: 34px; font-weight: 600; color: var(--callout-blue); line-height: 1;
  }
  .note {
    position: absolute; left: 434px; top: 795px;
    font-size: 31px; font-weight: 700; color: var(--ink); line-height: 1.27;
  }
  .brand {
    position: absolute; left: 0; right: 0; top: 1010px;
    display: flex; justify-content: center; align-items: center; gap: 14px;
  }
  .brand-dot { width: 34px; height: 34px; border-radius: 50%; background: var(--brand-blue); }
  .brand-name { font-size: 50px; font-weight: 800; color: var(--brand-blue); line-height: 1; }
</style>
</head>
<body>
<main class="poster">
  <svg class="backdrop" width="800" height="1200" viewBox="0 0 800 1200" aria-hidden="true">
    <rect width="800" height="1200" fill="var(--deep-blue)"/>
    <circle cx="930" cy="720" r="1010" fill="var(--mid-blue)"/>
    <circle cx="900" cy="700" r="880" fill="var(--pale-blue)"/>
    <circle cx="900" cy="760" r="830" fill="var(--mist-blue)"/>
  </svg>

  <h1 class="headline">Where</h1>
  <p class="subhead">does the <span class="emphasis">soap</span> go?</p>

  <div class="dispenser-photo" role="img" aria-label="Photo of the washer's open detergent dispenser tray with four compartments"></div>

  <svg class="callouts" width="800" height="1200" viewBox="0 0 800 1200" aria-hidden="true">
    <g stroke="var(--callout-blue)" stroke-width="4" stroke-linecap="round" fill="var(--callout-blue)">
      <line x1="472" y1="404" x2="185" y2="672"/>
      <line x1="472" y1="506" x2="242" y2="692"/>
      <line x1="472" y1="609" x2="182" y2="795"/>
      <line x1="472" y1="706" x2="272" y2="795"/>
      <circle cx="185" cy="672" r="10" stroke="none"/>
      <circle cx="242" cy="692" r="10" stroke="none"/>
      <circle cx="182" cy="795" r="10" stroke="none"/>
      <circle cx="272" cy="795" r="10" stroke="none"/>
    </g>
  </svg>

  <span class="label" style="top:380px">Fabric Softner</span>
  <span class="label" style="top:482px">Bleach</span>
  <span class="label" style="top:587px">Detergent</span>
  <span class="label" style="top:694px">Detergent</span>

  <p class="note">Please place pods<br>inside the washer.</p>

  <div class="brand">
    <span class="brand-dot"></span>
    <span class="brand-name">Tidal Lane</span>
  </div>
</main>
</body>
</html>
```